Stationery for Brightfield Pest Control
Business Cards, Letterhead, Envelopes, Folder, MemoPad, and E-Mail Signature
Stationery for Brightfield Pest Control  - Corporate Services
Creative Brief
Professional
Dana Pellborough
Owner
417 Calloway Street Marrowdale, ND, 58216
kmolegrove@mailvessel.com
www.gobrightfieldpest.com
VA Lic.#52734
I would like the be able to do editing to business cards and letterhead so that multiple peaple can use.
Concepts
Business Cards and Stationery for Background Check Company
Business Cards and Stationery for new compliance company.

```html
<!DOCTYPE html>
<html lang="en">
<head>
<meta charset="utf-8">
<title>Brightfield Pest Control – Business Cards</title>
<link rel="stylesheet" href="https://fonts.googleapis.com/css2?family=Open+Sans:wght@400;600;700&display=swap">
<style>
  :root {
    --stage: #dcd8d2;
    --paper: #ffffff;
    --paper-shade: #eeeeee;
    --green: #23903f;
    --green-dark: #166b2c;
    --green-light: #3bae56;
    --ink: #2b2b2b;
    --ink-soft: #6a6a6a;
    --silver: #c9cdca;
  }
  * { box-sizing: border-box; margin: 0; padding: 0; }
  html, body { width: 1200px; height: 730px; overflow: hidden; }
  body {
    background: var(--stage);
    font-family: "Open Sans", Arial, sans-serif;
    color: var(--ink);
    position: relative;
  }
  .card {
    position: absolute;
    width: 492px;
    height: 276px;
    border-radius: 14px;
    overflow: hidden;
    background: var(--paper);
    box-shadow: 0 6px 18px rgba(0,0,0,.22);
  }
  .card--front.card--solid { left: 72px; top: 60px; }
  .card--front.card--frost { left: 636px; top: 60px; }
  .card--back.card--solid { left: 72px; top: 408px; }
  .card--back.card--frost { left: 636px; top: 408px; }

  .card--frost {
    background: rgba(255,255,255,.55);
    box-shadow: 0 4px 14px rgba(0,0,0,.12);
    border: 1px solid rgba(255,255,255,.7);
  }

  .brand {
    position: absolute;
    left: 0; right: 0;
    display: flex;
    flex-direction: column;
    align-items: center;
  }
  .brand__row { display: flex; align-items: center; gap: 10px; }
  .brand__dot {
    width: 44px; height: 44px; border-radius: 50%;
    background: var(--green);
  }
  .brand__name {
    font-weight: 700;
    font-size: 25px;
    color: var(--green-dark);
    letter-spacing: -.2px;
    line-height: 1;
  }
  .brand__tagline {
    margin-top: 5px;
    margin-left: 54px;
    font-size: 7.5px;
    color: var(--ink-soft);
  }
  .card--front .brand { top: 38px; }
  .card--back .brand { top: 54px; }

  .name-band {
    position: absolute;
    left: 0; right: 0; top: 148px; height: 32px;
    background: linear-gradient(#fafafa, var(--paper-shade));
    border-bottom: 3px solid var(--silver);
    text-align: center;
    font-size: 9.5px;
    line-height: 30px;
  }
  .name-band__name { font-weight: 700; color: var(--ink); }
  .name-band__role { color: var(--ink-soft); }

  .green-band {
    position: absolute;
    left: 0; right: 0; bottom: 0;
    background: linear-gradient(var(--green-light), var(--green) 40%, var(--green-dark));
    color: #fff;
  }
  .green-band::before {
    content: "";
    position: absolute; left: 0; right: 0; top: 5px;
    height: 2px; background: rgba(255,255,255,.55);
  }
  .card--front .green-band { top: 186px; }
  .card--back .green-band { top: 170px; }

  .contact {
    position: absolute; left: 0; right: 0; top: 26px;
    display: flex; flex-direction: column; align-items: center; gap: 8px;
    font-size: 8.6px;
  }
  .contact__row { display: flex; gap: 12px; align-items: center; }
  .contact__item { display: inline-flex; align-items: center; gap: 4px; white-space: nowrap; }
  .contact__icon { width: 11px; height: 11px; flex: none; }

  .web {
    position: absolute; left: 0; right: 0; top: 44px;
    text-align: center; font-size: 11px; letter-spacing: 2.2px; color: #fff;
  }

  .card--frost .brand__dot { background: rgba(35,144,63,.8); }
  .card--frost .name-band { background: rgba(255,255,255,.35); border-bottom-color: rgba(201,205,202,.7); }
  .card--frost .green-band { opacity: .82; }

  .card--back.card--frost .brand { transform: scaleX(-1); opacity: .5; }
  .card--back.card--frost .brand__name { color: var(--ink-soft); }
  .card--back.card--frost .brand__dot { background: var(--green); }
</style>
</head>
<body>
<svg width="0" height="0" style="position:absolute" aria-hidden="true">
  <defs>
    <symbol id="icon-pin" viewBox="0 0 12 12"><circle cx="6" cy="6" r="6" fill="#fff"/><path d="M6 2.5a2.2 2.2 0 0 0-2.2 2.2C3.8 6.4 6 9.5 6 9.5s2.2-3.1 2.2-4.8A2.2 2.2 0 0 0 6 2.5z" fill="#23903f"/></symbol>
    <symbol id="icon-web" viewBox="0 0 12 12"><circle cx="6" cy="6" r="6" fill="#fff"/><circle cx="6" cy="6" r="3.4" fill="none" stroke="#23903f" stroke-width=".9"/><path d="M2.6 6h6.8M6 2.6c-1.6 2-1.6 4.8 0 6.8M6 2.6c1.6 2 1.6 4.8 0 6.8" fill="none" stroke="#23903f" stroke-width=".7"/></symbol>
    <symbol id="icon-phone" viewBox="0 0 12 12"><circle cx="6" cy="6" r="6" fill="#fff"/><path d="M4.2 3c.3 0 .5.2.6.4l.4 1c.1.2 0 .4-.1.6l-.4.4c.4.8 1 1.4 1.8 1.8l.4-.4c.2-.1.4-.2.6-.1l1 .4c.2.1.4.3.4.6v.8c0 .3-.3.6-.6.6C5.4 9.1 2.9 6.6 2.9 3.6c0-.3.3-.6.6-.6z" fill="#23903f"/></symbol>
    <symbol id="icon-mail" viewBox="0 0 12 12"><circle cx="6" cy="6" r="6" fill="#fff"/><rect x="3" y="4" width="6" height="4.2" rx=".4" fill="#23903f"/><path d="M3.2 4.3 6 6.4l2.8-2.1" fill="none" stroke="#fff" stroke-width=".6"/></symbol>
  </defs>
</svg>

<!-- front, solid -->
<section class="card card--front card--solid">
  <div class="brand">
    <div class="brand__row"><span class="brand__dot"></span><span class="brand__name">Brightfield Pest Control</span></div>
    <p class="brand__tagline">trusted care by local pest control professionals</p>
  </div>
  <div class="name-band"><span class="name-band__name">Dana Pellborough</span> <span class="name-band__role">| Owner</span></div>
  <div class="green-band">
    <div class="contact">
      <div class="contact__row">
        <span class="contact__item"><svg class="contact__icon"><use href="#icon-pin"/></svg>417 Calloway Street Marrowdale, ND, 58216</span>
        <span class="contact__item"><svg class="contact__icon"><use href="#icon-web"/></svg>www.gobrightfieldpest.com</span>
      </div>
      <div class="contact__row">
        <span class="contact__item"><svg class="contact__icon"><use href="#icon-phone"/></svg>701-555-2947</span>
        <span class="contact__item"><svg class="contact__icon"><use href="#icon-phone"/></svg>701-555-6182</span>
        <span class="contact__item"><svg class="contact__icon"><use href="#icon-phone"/></svg>701-555-4305</span>
        <span class="contact__item"><svg class="contact__icon"><use href="#icon-mail"/></svg>kmolegrove@mailvessel.com</span>
      </div>
    </div>
  </div>
</section>

<!-- front, frosted -->
<section class="card card--front card--frost">
  <div class="brand">
    <div class="brand__row"><span class="brand__dot"></span><span class="brand__name">Brightfield Pest Control</span></div>
    <p class="brand__tagline">trusted care by local pest control professionals</p>
  </div>
  <div class="name-band"><span class="name-band__name">Dana Pellborough</span> <span class="name-band__role">| Owner</span></div>
  <div class="green-band">
    <div class="contact">
      <div class="contact__row">
        <span class="contact__item"><svg class="contact__icon"><use href="#icon-pin"/></svg>417 Calloway Street Marrowdale, ND, 58216</span>
        <span class="contact__item"><svg class="contact__icon"><use href="#icon-web"/></svg>www.gobrightfieldpest.com</span>
      </div>
      <div class="contact__row">
        <span class="contact__item"><svg class="contact__icon"><use href="#icon-phone"/></svg>701-555-2947</span>
        <span class="contact__item"><svg class="contact__icon"><use href="#icon-phone"/></svg>701-555-6182</span>
        <span class="contact__item"><svg class="contact__icon"><use href="#icon-phone"/></svg>701-555-4305</span>
        <span class="contact__item"><svg class="contact__icon"><use href="#icon-mail"/></svg>kmolegrove@mailvessel.com</span>
      </div>
    </div>
  </div>
</section>

<!-- back, solid -->
<section class="card card--back card--solid">
  <div class="brand">
    <div class="brand__row"><span class="brand__dot"></span><span class="brand__name">Brightfield Pest Control</span></div>
    <p class="brand__tagline">trusted care by local pest control professionals</p>
  </div>
  <div class="green-band"><p class="web">www.GoBrightfieldPest.com</p></div>
</section>

<!-- back, frosted -->
<section class="card card--back card--frost">
  <div class="brand">
    <div class="brand__row"><span class="brand__dot"></span><span class="brand__name">Brightfield Pest Control</span></div>
    <p class="brand__tagline">trusted care by local pest control professionals</p>
  </div>
  <div class="green-band"><p class="web">www.GoBrightfieldPest.com</p></div>
</section>
</body>
</html>
```